Design a Brochure for IT Cloud company

This is an open idea type brochure design. I will attach our logo so that there's relevance, and brochure text to be arranged and placed in arrangement that your design will produce.....Ideally I would like a tri-fold brochure if possible [login to view URL]

```html
<!DOCTYPE html>
<html lang="en">
<head>
<meta charset="utf-8">
<title>Nimbus9 Tri-fold Brochure</title>
<link href="https://fonts.googleapis.com/css2?family=Open+Sans:wght@400;600;700&display=swap" rel="stylesheet">
<style>
  :root{
    --page:#e8e8e6;
    --paper:#ffffff;
    --ink:#4a4a4a;
    --ink-dark:#2d2d2d;
    --red:#d8322b;
    --red-dark:#b7201b;
    --blue:#1a6fc4;
    --blue-deep:#0b4f9e;
    --white:#ffffff;
  }
  *{box-sizing:border-box;margin:0;padding:0}
  html,body{width:1200px;height:900px;overflow:hidden}
  body{background:var(--page);font-family:"Open Sans",Arial,sans-serif;color:var(--ink)}
  .brochure{position:absolute;left:85px;top:83px;width:1038px;height:733px;display:flex;box-shadow:0 6px 18px rgba(0,0,0,.25)}
  .panel{width:346px;height:100%;position:relative;overflow:hidden}
  .panel--light{background:var(--paper)}
  .panel--light + .panel--light{border-left:1px solid #ececec}
  .panel--blue{background:linear-gradient(135deg,var(--blue) 0%,var(--blue-deep) 100%);color:var(--white)}
  .band{position:absolute;left:0;right:0;bottom:0;height:10px;background:linear-gradient(90deg,var(--blue-deep),var(--blue))}
  .blk{position:absolute;left:31px;right:28px}
  .panel--blue .blk{left:29px;right:24px}
  p{font-size:7.8px;line-height:15.3px}
  .pill{display:inline-block;background:linear-gradient(180deg,#ea4a40,var(--red-dark));color:var(--white);font-weight:700;font-size:13.5px;line-height:27px;height:27px;padding:0 26px;border-radius:14px;white-space:nowrap;box-shadow:0 2px 3px rgba(0,0,0,.2)}
  .pill--wide{font-size:12.5px;padding:0 20px}
  .sub{font-weight:700;font-size:10px;color:var(--ink-dark)}
  .dots{list-style:none}
  .dots li{font-size:7.8px;line-height:15px;padding-left:13px;position:relative}
  .dots li::before{content:"";position:absolute;left:0;top:5px;width:5px;height:5px;border-radius:50%;background:var(--red)}
  .bullets{list-style:disc;padding-left:10px}
  .bullets li{font-size:7.8px;line-height:15px}
  .art{position:absolute;background:linear-gradient(180deg,#cfd6dc,#8d979f);border-radius:6px}
  .art--servers{left:228px;top:301px;width:73px;height:112px}
  .art--cloud{left:43px;top:500px;width:253px;height:180px;background:linear-gradient(180deg,#8fd2f0 0%,#c9e5f2 45%,#55606a 100%)}
  .web{position:absolute;top:700px;left:0;right:0;text-align:center;font-size:12px;color:#555}
  .bh{font-size:21px;font-weight:700;white-space:nowrap}
  .ticks{list-style:none}
  .ticks li{position:relative;padding-left:17px;font-size:7.8px;line-height:15px;margin-bottom:2px}
  .ticks--big li{font-weight:600;font-size:9.3px;line-height:14px;margin-bottom:8px}
  .ticks svg{position:absolute;left:0;top:1px;width:11px;height:11px}
  .strong{font-weight:700}
  .rule{position:absolute;left:20px;right:20px;top:451px;height:2px;background:linear-gradient(90deg,transparent,rgba(255,255,255,.9),transparent)}
  .bsub{font-size:12.5px;font-weight:700}
</style>
</head>
<body>
<svg width="0" height="0" style="position:absolute"><defs><symbol id="tick" viewBox="0 0 14 14"><path d="M1.5 7.5l3.5 3.5 7.5-9" fill="none" stroke="#fff" stroke-width="2.4" stroke-linecap="round" stroke-linejoin="round"/></symbol></defs></svg>
<main class="brochure">
  <section class="panel panel--light">
    <h2 class="blk" style="top:31px"><span class="pill">Business Online</span></h2>
    <p class="blk" style="top:69px">Nimbus9 Enterprise Systems is a privately owned company that provides Cloud leading technology solutions across a wide range of industries throughout Australia and Asia Pacific.</p>
    <p class="blk" style="top:127px">Based in beautiful Sydney, our business, structure and technology solutions are all designed to help customers meet their business objectives. We design, engineer and manage technology solutions through our specialist businesses which are Cloud Solutions, Integrated Solutions and Managed Services.Our Consulting and Service Delivery Teams based on a wealth of Technical and Business Knowledge, enable our customers to align their ICT programs with their business objectives Your corporate data is safe and secure in two of Australia's premier datacentres, protected by technology and practises small businesses generally cannot afford.</p>
    <h2 class="blk" style="top:301px"><span class="pill">Our CORE Business</span></h2>
    <div class="art art--servers" role="img" aria-label="Illustration of server towers on a stack of storage disks"></div>
    <ul class="dots blk" style="top:343px;right:130px">
      <li>CLOUD COMPUTING:</li>
      <li>ONLINE DESKTOPas a SERVICE Daas</li>
      <li>DISASTER RECOVERYas a SERVICE DRaaS</li>
      <li>INFRASTRUCTURE as a SERVICE IaaS</li>
      <li>BACKUPas a SERVICE BaaS</li>
      <li>INTEGRATION / SUPPORT</li>
    </ul>
    <h2 class="blk" style="top:461px"><span class="pill pill--wide">Our SOLUTIONS to your IT CHALLENGES</span></h2>
    <h3 class="sub blk" style="top:504px">Online Desktop</h3>
    <p class="blk" style="top:525px">Do you want to stop agonising about:</p>
    <ul class="dots blk" style="top:547px">
      <li>Your email systems and compliance?</li>
      <li>Your server hardware warranty?</li>
      <li>Your desktop software and patching levels?</li>
      <li>Northgate licensing?</li>
    </ul>
    <p class="blk" style="top:624px">If you do, the Nimbus9 Online Desktop is for you. For a fixed price per month per user, you can move all your IT into our CLOUD and remove ALL YOUR ANXIETY. You'll know that your data is SAFE and SECURE in our two datacentres.</p>
    <div class="band"></div>
  </section>

  <section class="panel panel--light">
    <p class="blk" style="top:30px">And the best bit is that billing is month-to-month. You PAY for what you USE, no lock in contracts – scale up or down depending on the amount of users in any given month.</p>
    <h2 class="blk" style="top:103px"><span class="pill">Backup and Disaster Recovery</span></h2>
    <h3 class="sub blk" style="top:141px">Backup:</h3>
    <p class="blk" style="top:164px">Do you need to back up with a minimum amount of stress and reliance on tapes? Nimbus9 has the infrastructure to store backups of your data in a secure container, accessible only by you. Just select the amount of storage, ascertain that you internet link is sufficient and you can back up to one of our world-class datacentres.<br>As a further level of protection we mirror all your backups to our seconddatacentre to provide OPTIMUM REDUNDANCY.</p>
    <h3 class="sub blk" style="top:280px">Disaster Recovery:</h3>
    <p class="blk" style="top:306px">Can you afford downtime on your production systems for any reason? Will your business suffer? These are the questions facing all small business owners today. There are some sobering statistics about data loss and business interruption and inactivity.<br>Nimbus9 disaster recovery solutions are elastically designed to be tailored to your business</p>
    <ul class="bullets blk" style="top:412px">
      <li>REDUNDANCY across two datacentres</li>
      <li>CUSTOMISED to your business</li>
      <li>SYSTEMS ACCESS by Remote functionality if a DR situation develops</li>
      <li>USAGE LICENSING (if the DR is not being used by users, cost to you is lower)</li>
    </ul>
    <div class="art art--cloud" role="img" aria-label="Illustration of a cloud connected to laptops, desktop computers, tablet and phone"></div>
    <div class="web">www.nimbus9.com.au</div>
    <div class="band"></div>
  </section>

  <section class="panel panel--blue">
    <h2 class="bh blk" style="top:22px">Infrastructure as a Service</h2>
    <p class="blk" style="top:58px">You've tried the public clouds like Skyline Web Services and Northgate's Cumulus and have found the exact same problems as Nimbus9 did:</p>
    <ul class="ticks blk" style="top:98px">
      <li><svg><use href="#tick"/></svg>Zero geometric benefit – they simply don't provide discount through volume AMI/image purchase</li>
      <li><svg><use href="#tick"/></svg>No-one to help</li>
    </ul>
    <p class="blk" style="top:148px">Nimbus9 understands. Our engineers can be hands-on or hands-off on your infrastructure in our public cloud – it's up to you.</p>
    <p class="blk" style="top:192px">Our engineers can provide best practise implementations in a wide variety of fields including but not limited to:</p>
    <ul class="ticks ticks--big blk" style="top:237px">
      <li><svg><use href="#tick"/></svg>TalkLink</li>
      <li><svg><use href="#tick"/></svg>MailHub</li>
      <li><svg><use href="#tick"/></svg>TeamShare</li>
      <li><svg><use href="#tick"/></svg>SQL/File Clustering</li>
      <li><svg><use href="#tick"/></svg>SQL/File Clustering</li>
      <li><svg><use href="#tick"/></svg>Open Source load balancing</li>
      <li><svg><use href="#tick"/></svg>Open Source mail relaying to MailHub.</li>
    </ul>
    <p class="strong blk" style="top:400px">If you need to build an infrastructure as a service cloud – let us help you.</p>
    <div class="rule"></div>
    <h2 class="bh blk" style="top:480px">Integration and Support</h2>
    <h3 class="bsub blk" style="top:513px">Integration:</h3>
    <p class="blk" style="top:542px">Nimbus9 offers full service network integration and support.We PLAN, DESIGN, DEPLOY and OPTIMISE IT Networks taking into consideration all aspects of your existing environment and developing the right solution to fit your needs.<br>Our solutions deliver LAN, WAN and wireless connectivity between people, locations and systems both inside and outside your organisation.</p>
    <h3 class="bsub blk" style="top:621px">Support:</h3>
    <p class="blk" style="top:648px">Nimbus9deliversflexible and cost-effective support solutions. All provided from our Australian-based support desk 24 hours a day, 365 days a year.</p>
  </section>
</main>
</body>
</html>
```